Design Creative Banner or Gif Ads. 3 Designs To Be Selected

Come up with some creative banner ads for stonewell.co.nz

*At least 3 different winning banners will be chosen*

Please provide banner ads / gif ads in common google ads / website banner formats.

They can be gif or static but must stand out while still maintaining clear clean text and visuals, with a premium professional feel (please avoid clip art or anything that gives a cheap message).

Please keep in mind that these will likely be small ads so text needs to be large and if there's there a lot of text then use multiple frames/ pages as submit as a gif.

Style
Minimal & clean lines
Architectural or realistic images
Avoid cartoon styles, clipart, or anything that looks cheap

Font
Nexa or Montserrat or similar

Tone
Premium, serious, trustworthy — fits new builds

Colours
Option 1: Deep Navy (trust & quality) & lighter blues and warm grey
Option 2: Open to bright colours to help the ads stand out, such as (but not limited to) bright pink with black, yellow, fluorescent green, provided the messaging is still done professionally.
Our logo is attached (Stone Well Logo)

Display Sizes
Ad specs for file sizes should be file formats like JPEG, GIF, and PNG, with animations limited to a max of 30 seconds or less.
We will need several different ad sizes provided for each of the 3 selected winning designs.

• Medium Rectangle: 300 × 250 pixels
• Leaderboard: 728 × 90 pixels
• Desktop Banner ad image: (640x360 pixels)
• Desktop Banner ad image 2: (300x600 pixels)
• Possibly one or two other sizes

Flexibility to be creative
The ad text, words, upper/lower case, layout, colour, theme, and images can be adjusted to how you think it will look best. The follow example ads are just examples of what we are after but we are keen to see what you can create.

Recommendations at this point:
1. Avoid text heavy
2. Looking for more Gif ads
3. Imaging: if possible use real stock photo's rather than AI

Themes:

1
Building Soon? Start Here
Free Build Planning Pack:
✓ Build Cost Calculator
✓ Hidden Cost Checklist
✓ Builder Comparison Guide
Build With Confidence
Download Free

2
Before You Choose A Builder
Compare Price, Scope, Risk & Value
Avoid Costly Mistakes
Choose The Right Builder With Confidence
Download The Free Guide

3
Planning A New Build?
Avoid These Common Mistakes:
✗ Hidden Exclusions
✗ Missing Scope
✗ Unrealistic Allowances
✗ Budget Blowouts
Download The Free Guide

4
Before You Buy Land
Know what it could cost to build.
Avoid Costly Building Mistakes
Download Our Free Guides

5
Know Your Build Budget?
• Free Build Cost Calculator
• Hidden Cost Checklist
• Build Planning Tools
Calculate Costs (Download)

Target Market(s)

Landowners looking to build

Industry/Entity Type

Building

Font styles to use
Other font styles liked:
• Nexa or Montserrat or similar

Requirements
Should not have
• Avoid cartoon styles, clipart, or anything that looks cheap

```html
<!DOCTYPE html>
<html lang="en">
<head>
<meta charset="utf-8">
<title>Stone Well – Animated GIF Banner Ad</title>
<link href="https://fonts.googleapis.com/css2?family=Montserrat:wght@500;600;700;800;900&display=swap" rel="stylesheet">
<style>
  :root {
    --navy: #17304f;
    --navy-deep: #1b3350;
    --sky: #3399c6;
    --sky-bright: #4aaee6;
    --tagline: #6f9bc0;
    --white: #ffffff;
    --photo-warm: #6b5a4d;
    --photo-grey: #7d7b76;
    --photo-blue: #4f7fae;
  }
  * { margin: 0; padding: 0; box-sizing: border-box; }
  html, body { width: 840px; height: 1200px; overflow: hidden; background: var(--white); }
  body { position: relative; font-family: "Montserrat", sans-serif; color: var(--navy); }

  .brand { position: absolute; left: 61px; top: 26px; display: flex; align-items: center; gap: 26px; }
  .brand-mark { width: 80px; height: 70px; background: var(--navy); }
  .brand-name { font-size: 42px; font-weight: 700; color: var(--navy); line-height: 1; letter-spacing: -0.5px; }
  .brand-tagline { position: absolute; left: 166px; top: 87px; font-size: 10.5px; font-weight: 700; color: var(--tagline); letter-spacing: 0.1px; }

  .headline { position: absolute; left: 44px; top: 189px; font-size: 93px; font-weight: 800; line-height: 115px; color: var(--navy); letter-spacing: -1px; }
  .format { position: absolute; left: 45px; top: 438px; font-size: 38px; font-weight: 500; color: var(--navy); letter-spacing: -0.5px; }

  .banner { position: absolute; left: 34px; top: 546px; width: 454px; height: 376px; border: 2px solid #222; overflow: hidden; background: var(--navy-deep); }
  .banner-photo { position: absolute; inset: 0;
    background:
      linear-gradient(90deg, var(--navy-deep) 0%, var(--navy-deep) 36%, rgba(27,51,80,0.55) 56%, rgba(27,51,80,0) 70%),
      linear-gradient(160deg, #4a5560 0%, var(--photo-grey) 30%, var(--photo-blue) 55%, #5d564f 78%, var(--photo-warm) 100%); }
  .banner-brand { position: absolute; left: 27px; top: 20px; display: flex; align-items: center; gap: 10px; }
  .banner-brand-mark { width: 36px; height: 30px; background: var(--white); }
  .banner-brand-name { font-size: 19px; font-weight: 700; color: var(--white); }
  .banner-brand-tagline { position: absolute; left: 74px; top: 55px; font-size: 4px; font-weight: 700; color: var(--white); opacity: .8; }
  .banner-rule { position: absolute; left: 29px; top: 90px; width: 62px; height: 5px; background: var(--sky-bright); border-radius: 2px; }
  .banner-title { position: absolute; left: 28px; top: 112px; font-size: 34px; font-weight: 900; line-height: 32.5px; color: var(--white); letter-spacing: -0.8px; }
  .banner-title .accent { color: var(--sky-bright); }
  .banner-copy { position: absolute; left: 28px; top: 256px; font-size: 18px; font-weight: 800; line-height: 22.4px; color: var(--white); letter-spacing: -0.2px; }

  .about-title { position: absolute; left: 27px; top: 976px; font-size: 61px; font-weight: 500; color: var(--sky); letter-spacing: -1px; }
  .about-text { position: absolute; left: 45px; top: 1090px; font-size: 29px; font-weight: 500; line-height: 37px; color: var(--sky); }
</style>
</head>
<body>
  <header class="brand">
    <span class="brand-mark"></span>
    <span class="brand-name">Stone Well</span>
  </header>
  <p class="brand-tagline">COMPARE QUOTES FROM TRUSTED BUILDERS</p>

  <h1 class="headline">ANIMATED GIF<br>BANNER AD</h1>
  <p class="format">250 x 300 web banner</p>

  <section class="banner">
    <div class="banner-photo" role="img" aria-label="Photo of a softly lit interior with a blue planning guide booklet standing on a timber table"></div>
    <div class="banner-brand">
      <span class="banner-brand-mark"></span>
      <span class="banner-brand-name">Stone Well</span>
    </div>
    <p class="banner-brand-tagline">COMPARE QUOTES FROM TRUSTED BUILDERS</p>
    <span class="banner-rule"></span>
    <h2 class="banner-title">FREE<br>BUILD<br><span class="accent">PLANNING</span><br>PACK</h2>
    <p class="banner-copy">Calculator,<br>checklist and<br>builder guide.</p>
  </section>

  <h2 class="about-title">ABOUT THIS AD</h2>
  <p class="about-text">This is an animated GIF (motion) banner ad<br>designed for web&nbsp;&nbsp;&nbsp;placements.</p>
</body>
</html>
```